Web Page Design for a Website that Provides Tutoring

I am looking to create an online tutoring website. The website will allow parents or students to contact tutors with a view to instructing them to tutor themselves or their children.

The name of the website is LendYourLessons.

This brief is to create the design for one of the web pages for this web site. I am hoping the same designer will be available to design other pages.

The page I want designed is one of the more complex and I have attached the design as an excel spreadsheet. The web page needs to include all the items on this page but if you want to change the positioning of the items then Im fine with that.

I recently had two logos created for this website. My favourite is the one with a mortar board but im not sure I like the colours. I have attached both of these logos and you can use either of them, change the colours or create something different. I just want a design pleasing to the eye. If the logo is changed I would like that in a seperate file.

So can you please submit designs for this page. I have attached the two logos which you can use, change or if you feel you have a better idea then you can use that.

On the spreadsheet the Send Message, Favourite etc are buttons.

Target Market(s)

People who want to better themselves.
Possible middle class to upper class.

Industry/Entity Type

Tutoring

Number of Pages Required

1 page

Requirements
Must have
• The designs must have alot of the information attached in the spreadsheet.

```html
<!DOCTYPE html>
<html lang="en">
<head>
<meta charset="utf-8">
<title>LendYourLessons – Learn Today, Succeed Tomorrow</title>
<link rel="stylesheet" href="https://fonts.googleapis.com/css2?family=Roboto:wght@300;400;500;700&display=swap">
<style>
:root{
  --navy:#3a5d99;
  --orange:#f26a3d;
  --amber:#f7931e;
  --maths:#f4603e;
  --history:#fbb515;
  --english:#3f6b22;
  --geography:#4a90f0;
  --chemistry:#21d64b;
  --biology:#3a5d99;
  --physics:#f79421;
  --others:#c1440e;
  --ink:#333;
  --muted:#777;
  --white:#fff;
}
*{box-sizing:border-box;margin:0;padding:0}
html,body{width:1200px;height:3509px;overflow:hidden}
body{font-family:'Roboto',Arial,sans-serif;color:var(--ink);background:var(--white);position:relative}
.abs{position:absolute}
a{color:inherit;text-decoration:none}

/* header / hero */
.hero{position:absolute;left:0;top:0;width:1200px;height:627px;
  background:linear-gradient(180deg,#c9ccd0 0%,#e4e3df 40%,#b9aa98 72%,#7d6a58 100%)}
.hero-scene{position:absolute;inset:0}
.logo{position:absolute;left:82px;top:22px;display:flex;align-items:center;gap:8px;
  font-size:30px;font-weight:700;color:var(--orange)}
.logo-mark{width:16px;height:16px;background:var(--navy)}
.nav{position:absolute;top:30px;left:540px;display:flex;align-items:center;gap:0}
.nav a{font-size:15px;color:var(--navy);margin-right:22px}
.nav a.is-active{color:var(--navy);font-weight:500}
.btn{display:inline-flex;align-items:center;justify-content:center;height:32px;padding:0 20px;
  font-size:15px;color:var(--white);border-radius:2px}
.btn-login{background:var(--orange);margin-right:14px}
.btn-register{background:var(--navy)}
.hero-title{position:absolute;left:80px;top:280px;font-weight:300;font-size:66px;line-height:72px}
.hero-title .l1{color:var(--navy);display:block}
.hero-title .l2{color:var(--orange);display:block}
.hero-actions{position:absolute;left:82px;top:449px;display:flex;gap:14px}
.hero-actions .btn{height:48px;padding:0 22px;font-size:15px;gap:10px}
.hero-actions .tutor{background:var(--navy)}
.hero-actions .student{background:var(--orange)}

/* section titles */
.sec-title{position:absolute;left:0;width:1200px;text-align:center;font-size:27px;color:var(--navy)}
.sec-title em{font-style:normal;color:var(--orange)}
.divider{position:absolute;left:520px;width:160px;height:14px}

/* features */
.feature{position:absolute;width:257px;text-align:center}
.feature .art{width:130px;height:94px;margin:0 auto;border-radius:4px}
.feature h3{font-size:16px;font-weight:400;margin-top:24px;color:var(--ink)}
.feature p{font-size:12.5px;color:var(--muted);line-height:20px;margin-top:10px}

/* banners */
.banner{position:absolute;left:0;width:1200px;height:82px;background:var(--navy);color:var(--white);
  display:flex;align-items:center;justify-content:center;font-size:26px}

/* subjects */
.subjects{position:absolute;left:0;top:1134px;width:1200px;display:grid;
  grid-template-columns:repeat(4,300px);grid-auto-rows:240px}
.subject{position:relative;color:var(--white);text-align:center;border-right:1px solid rgba(255,255,255,.5);border-bottom:1px solid rgba(255,255,255,.5)}
.subject h3{font-size:28px;font-weight:400;margin-top:46px}
.subject svg{position:absolute;left:105px;top:106px;width:90px;height:90px}
.s-maths{background:var(--maths)}.s-history{background:var(--history)}
.s-english{background:var(--english)}.s-geography{background:var(--geography)}
.s-chemistry{background:var(--chemistry)}.s-biology{background:var(--biology)}
.s-physics{background:var(--physics)}.s-others{background:var(--others)}

/* steps */
.step{position:absolute;width:257px;text-align:center;top:1768px}
.step .dot{width:112px;height:112px;border-radius:50%;background:var(--amber);margin:0 auto}
.step h3{font-size:16px;font-weight:400;margin-top:28px}
.step p{font-size:12.5px;color:var(--muted);line-height:20px;margin-top:10px}

/* audiences */
.audience{position:absolute;top:2124px;height:409px;color:var(--white);text-align:center;padding:48px 34px 0}
.audience .ring{width:106px;height:106px;border:2px solid rgba(255,255,255,.85);border-radius:50%;margin:0 auto;display:flex;align-items:center;justify-content:center}
.audience h3{font-size:27px;font-weight:400;margin-top:20px}
.audience p{font-size:13px;line-height:23px;margin-top:12px}
.a-parents{left:0;width:428px;background:var(--maths)}
.a-students{left:428px;width:344px;background:var(--navy)}
.a-tutors{left:772px;width:428px;background:var(--physics)}

/* testimonials */
.quote{position:absolute;left:116px;top:2680px;width:968px;font-size:15px;line-height:33px;color:var(--muted)}
.qmark{position:absolute;font-size:72px;font-weight:700;color:var(--navy);line-height:1}
.name-tag{position:absolute;left:498px;top:2774px;width:204px;height:52px;background:var(--amber);color:var(--white);text-align:center;padding-top:7px}
.name-tag strong{display:block;font-size:14px;font-weight:500}
.name-tag span{display:block;font-size:11px}
.name-tag::after{content:"";position:absolute;left:94px;bottom:-10px;border:8px solid transparent;border-top-color:var(--amber);border-bottom:0}
.avatar{position:absolute;border-radius:50%}
.av-sm{width:96px;height:96px;top:2899px}
.av-lg{width:164px;height:164px;top:2865px;left:517px;background:#7c8794;border:3px solid #fff;box-shadow:0 0 0 1px #ddd}

/* footer */
.footer{position:absolute;left:0;top:3076px;width:1200px;height:381px;
  background:linear-gradient(160deg,#4c6ea8 0%,#3a5d99 55%,#2f4f86 100%);color:var(--white)}
.footer h4{font-size:21px;font-weight:400;color:var(--amber);position:absolute;top:62px}
.footer .rule{position:absolute;top:98px;height:1px;background:rgba(255,255,255,.3)}
.f-links{position:absolute;left:82px;top:112px;list-style:none;font-size:13px;line-height:26.5px}
.f-links li::before{content:"›";margin-right:6px}
.f-contact{position:absolute;left:304px;top:114px;width:300px;font-size:12.5px;line-height:19px}
.f-contact .row{display:flex;gap:12px;margin-bottom:14px}
.f-contact .ico{flex:none;width:14px;height:14px;margin-top:2px}
.f-contact .phone{color:var(--amber);font-size:16px;font-weight:500}
.f-news{position:absolute;left:641px;top:114px;width:205px;font-size:10.5px;line-height:16px}
.f-news .field{margin-top:14px;height:26px;background:var(--white);color:#888;font-size:11px;padding:6px 8px}
.f-news .subscribe{display:inline-block;margin-top:14px;background:var(--orange);color:#fff;font-size:11px;padding:5px 12px}
.f-social{position:absolute;left:933px;top:118px;list-style:none;font-size:13px}
.f-social li{display:flex;align-items:center;gap:12px;height:34px}
.f-social .sq{width:22px;height:22px;background:rgba(255,255,255,.9)}
.bottom-bar{position:absolute;left:0;top:3457px;width:1200px;height:52px;background:var(--amber);color:var(--white);font-size:11.5px;display:flex;align-items:center;padding:0 82px;justify-content:space-between}
.bottom-bar nav a{margin-left:26px}
</style>
</head>
<body>

<header class="hero">
  <div class="hero-scene" role="img" aria-label="Photo of a young student sitting on a wooden deck with a laptop, a hot air balloon in a cloudy sky"></div>
  <div class="logo"><span class="logo-mark"></span>LendYourLessons</div>
  <nav class="nav">
    <a class="is-active" href="#">Home</a><a href="#">About</a><a href="#">Search</a><a href="#">Student</a><a href="#">Tutor</a><a href="#">Contacts</a>
    <a class="btn btn-login" href="#">Log In</a><a class="btn btn-register" href="#">Register</a>
  </nav>
  <h1 class="hero-title"><span class="l1">Learn Today</span><span class="l2">Succeed Tomorrow</span></h1>
  <div class="hero-actions">
    <a class="btn tutor" href="#"><svg width="16" height="22" viewBox="0 0 16 22" fill="#fff"><circle cx="8" cy="4" r="3.5"/><rect x="4" y="9" width="8" height="12" rx="2"/></svg>I am a tutor</a>
    <a class="btn student" href="#"><svg width="18" height="20" viewBox="0 0 18 20" fill="#fff"><circle cx="9" cy="5" r="4"/><path d="M1 20c0-6 4-9 8-9s8 3 8 9z"/></svg>I am a student</a>
  </div>
</header>

<section class="careers">
  <h2 class="sec-title" style="top:672px">Helping People To <em>Grow Their Careers</em></h2>
  <svg class="divider" style="top:721px" viewBox="0 0 160 14"><line x1="0" y1="7" x2="160" y2="7" stroke="#ddd"/><path d="M70 9 Q80 1 90 9" fill="none" stroke="#bbb" stroke-width="2"/></svg>
  <div class="feature" style="left:86px;top:802px">
    <div class="art" role="img" aria-label="Illustration of a teacher pointing at a board" style="background:linear-gradient(135deg,#f7931e,#3a5d99)"></div>
    <h3>Learn From The Experts</h3>
    <p>Neque porro quisquam est qui dolorem adipisci velit. There is no one who loves pain itself, who seeks after it.</p>
  </div>
  <div class="feature" style="left:471px;top:802px">
    <div class="art" role="img" aria-label="Illustration of a figure climbing steps" style="background:linear-gradient(135deg,#f7931e,#f26a3d)"></div>
    <h3>Guaranteed Career Growth</h3>
    <p>Neque porro quisquam est qui dolorem adipisci velit. There is no one who loves pain itself, who seeks after it.</p>
  </div>
  <div class="feature" style="left:864px;top:802px">
    <div class="art" role="img" aria-label="Illustration of a framed certificate" style="background:linear-gradient(135deg,#3a5d99,#f26a3d)"></div>
    <h3>Trusted &amp; Certified</h3>
    <p>Neque porro quisquam est qui dolorem adipisci velit. There is no one who loves pain itself, who seeks after it.</p>
  </div>
</section>

<div class="banner" style="top:1053px">Take A look At Our Inspiring Tutors In Some Of Our Core Subject Areas</div>

<section class="subjects">
  <div class="subject s-maths"><h3>Maths</h3>
    <svg viewBox="0 0 90 90" fill="#fff"><rect x="2" y="2" width="40" height="40" rx="5"/><rect x="48" y="2" width="40" height="40" rx="5"/><rect x="2" y="48" width="40" height="40" rx="5"/><rect x="48" y="48" width="40" height="40" rx="5"/>
      <g stroke="var(--maths)" stroke-width="5" stroke-linecap="round"><line x1="12" y1="22" x2="32" y2="22"/><line x1="58" y1="22" x2="78" y2="22"/><line x1="68" y1="12" x2="68" y2="32"/><line x1="14" y1="60" x2="30" y2="76"/><line x1="30" y1="60" x2="14" y2="76"/><line x1="58" y1="68" x2="78" y2="68"/></g>
      <circle cx="68" cy="58" r="3.5" fill="var(--maths)"/><circle cx="68" cy="78" r="3.5" fill="var(--maths)"/></svg></div>
  <div class="subject s-history"><h3>History</h3>
    <svg viewBox="0 0 90 90" fill="none" stroke="#fff" stroke-width="5"><line x1="18" y1="6" x2="72" y2="6"/><line x1="18" y1="84" x2="72" y2="84"/><path d="M24 6 Q24 34 45 45 Q66 34 66 6"/><path d="M24 84 Q24 56 45 45 Q66 56 66 84"/><path d="M30 80 Q45 62 60 80Z" fill="#fff"/></svg></div>
  <div class="subject s-english"><h3>English</h3>
    <svg viewBox="0 0 90 90" fill="#fff"><rect x="8" y="60" width="74" height="16" rx="3"/><rect x="14" y="42" width="66" height="14" rx="3"/><rect x="6" y="24" width="70" height="14" rx="3"/><path d="M20 6h40l10 14H30z"/></svg></div>
  <div class="subject s-geography"><h3>Geography</h3>
    <svg viewBox="0 0 90 90" fill="none" stroke="#fff" stroke-width="4"><circle cx="45" cy="38" r="26" fill="#fff"/><path d="M16 38a29 29 0 0 0 52 18"/><line x1="45" y1="68" x2="45" y2="80"/><line x1="30" y1="84" x2="60" y2="84"/></svg></div>
  <div class="subject s-chemistry"><h3>Chemistry</h3>
    <svg viewBox="0 0 90 90" fill="none" stroke="#fff" stroke-width="4"><path d="M34 6h22M38 6v26L16 80h58L52 32V6"/><path d="M26 62h38l8 16H18z" fill="#fff"/></svg></div>
  <div class="subject s-biology"><h3>Biology</h3>
    <svg viewBox="0 0 90 90" stroke="#fff" stroke-width="4" fill="#fff"><line x1="45" y1="45" x2="16" y2="22"/><line x1="45" y1="45" x2="72" y2="18"/><line x1="45" y1="45" x2="18" y2="72"/><line x1="45" y1="45" x2="74" y2="70"/><line x1="45" y1="45" x2="80" y2="45"/><circle cx="45" cy="45" r="10"/><circle cx="16" cy="22" r="7"/><circle cx="72" cy="18" r="7"/><circle cx="18" cy="72" r="7"/><circle cx="74" cy="70" r="7"/><circle cx="80" cy="45" r="5"/></svg></div>
  <div class="subject s-physics"><h3>Physics</h3>
    <svg viewBox="0 0 90 90" fill="none" stroke="#fff" stroke-width="4"><ellipse cx="45" cy="45" rx="40" ry="15"/><ellipse cx="45" cy="45" rx="40" ry="15" transform="rotate(60 45 45)"/><ellipse cx="45" cy="45" rx="40" ry="15" transform="rotate(-60 45 45)"/><circle cx="45" cy="45" r="6" fill="#fff"/></svg></div>
  <div class="subject s-others"><h3>Others</h3>
    <svg viewBox="0 0 90 90"><circle cx="45" cy="45" r="38" fill="#fff"/><circle cx="28" cy="45" r="6" fill="var(--others)"/><circle cx="45" cy="45" r="6" fill="var(--others)"/><circle cx="62" cy="45" r="6" fill="var(--others)"/></svg></div>
</section>

<section class="steps">
  <h2 class="sec-title" style="top:1657px">New To <em>Online Tution</em></h2>
  <svg class="divider" style="top:1706px" viewBox="0 0 160 14"><line x1="0" y1="7" x2="160" y2="7" stroke="#ddd"/><path d="M70 9 Q80 1 90 9" fill="none" stroke="#bbb" stroke-width="2"/></svg>
  <div class="step" style="left:86px"><div class="dot"></div><h3>1. Search For Subject</h3><p>Neque porro quisquam est qui dolorem adipisci velit. There is no one who loves pain itself, who seeks after it.</p></div>
  <div class="step" style="left:471px"><div class="dot"></div><h3>2. Choose A Tutor</h3><p>Neque porro quisquam est qui dolorem adipisci velit. There is no one who loves pain itself, who seeks after it.</p></div>
  <div class="step" style="left:864px"><div class="dot"></div><h3>3. Enjoy Learning</h3><p>Neque porro quisquam est qui dolorem adipisci velit. There is no one who loves pain itself, who seeks after it.</p></div>
</section>

<div class="banner" style="top:2042px">A Personalized Tutoring Solution To Fit your Tution Needs</div>

<section class="audiences">
  <div class="audience a-parents">
    <div class="ring"><svg width="54" height="60" viewBox="0 0 54 60" fill="#fff"><circle cx="18" cy="8" r="7"/><rect x="10" y="17" width="16" height="24" rx="4"/><rect x="11" y="38" width="6" height="22"/><rect x="19" y="38" width="6" height="22"/><circle cx="42" cy="26" r="5"/><rect x="36" y="33" width="12" height="16" rx="3"/><rect x="37" y="46" width="4" height="14"/><rect x="43" y="46" width="4" height="14"/></svg></div>
    <h3>Parents</h3>
    <p>If you are going to use a passage of Lorem Ipsum, you need to be sure there isn't anything embarrassing hidden in the middle of text. All the Lorem Ipsum generators on the Internet tend to repeat predefined chunks as necessary, making this the first true generator on the Internet.</p>
  </div>
  <div class="audience a-students">
    <div class="ring"><svg width="62" height="44" viewBox="0 0 62 44" fill="#fff"><path d="M31 0l14 6-14 6-14-6z"/><circle cx="31" cy="18" r="6"/><path d="M21 44c0-10 4-15 10-15s10 5 10 15z"/><circle cx="11" cy="20" r="5"/><path d="M2 44c0-9 4-13 9-13s8 3 9 7v6z"/><circle cx="51" cy="20" r="5"/><path d="M42 44v-6c1-4 4-7 9-7s9 4 9 13z"/></svg></div>
    <h3>Students</h3>
    <p>If you are going to use a passage of Lorem Ipsum, you need to be sure there isn't anything embarrassing hidden in the middle of text. All the Lorem Ipsum generators on the Internet tend to repeat predefined chunks as necessary, making this the first true generator on the Internet.</p>
  </div>
  <div class="audience a-tutors">
    <div class="ring"><svg width="60" height="56" viewBox="0 0 60 56" fill="none" stroke="#fff" stroke-width="3"><rect x="4" y="4" width="32" height="24"/><circle cx="46" cy="14" r="5" fill="#fff"/><path d="M40 24h12v16h-3v16h-6V40h-3z" fill="#fff"/><line x1="40" y1="26" x2="30" y2="18"/></svg></div>
    <h3>Tutors</h3>
    <p>If you are going to use a passage of Lorem Ipsum, you need to be sure there isn't anything embarrassing hidden in the middle of text. All the Lorem Ipsum generators on the Internet tend to repeat predefined chunks as necessary, making this the first true generator on the Internet.</p>
  </div>
</section>

<section class="testimonials">
  <h2 class="sec-title" style="top:2583px">Student’s <em>Testimonials</em></h2>
  <svg class="divider" style="top:2632px" viewBox="0 0 160 14"><line x1="0" y1="7" x2="160" y2="7" stroke="#ddd"/><path d="M70 9 Q80 1 90 9" fill="none" stroke="#bbb" stroke-width="2"/></svg>
  <span class="qmark" style="left:80px;top:2664px">“</span>
  <p class="quote">It is immediately obvious that access to behaviour data is far easier in Beacon than it is in ClassDesk. However, improving behaviour management is not just about having access to data, it is about having access to meaningful data. Beacon gives us just that</p>
  <span class="qmark" style="left:1090px;top:2702px">”</span>
  <div class="name-tag"><strong>Daniel Reed Porter</strong><span>Student, City College</span></div>
  <div class="avatar av-sm" style="left:81px;background:#6d6a66" role="img" aria-label="Student portrait"></div>
  <div class="avatar av-sm" style="left:219px;background:#7cb83a" role="img" aria-label="Student portrait"></div>
  <div class="avatar av-sm" style="left:366px;background:#a9b4b8" role="img" aria-label="Student portrait"></div>
  <div class="avatar av-lg" role="img" aria-label="Portrait of the featured student"></div>
  <div class="avatar av-sm" style="left:736px;background:#7cb83a" role="img" aria-label="Student portrait"></div>
  <div class="avatar av-sm" style="left:883px;background:#5a4a40" role="img" aria-label="Student portrait"></div>
  <div class="avatar av-sm" style="left:1028px;background:#8d8a88" role="img" aria-label="Student portrait"></div>
</section>

<footer class="footer" role="img" aria-label="Footer backdrop of hands typing on a laptop in blue tones">
  <h4 style="left:82px">Quick Links</h4>
  <div class="rule" style="left:82px;width:150px"></div>
  <ul class="f-links">
    <li>Home</li><li>About</li><li>Search</li><li>Student</li><li>Tutor</li><li>Contacts</li>
  </ul>
  <h4 style="left:304px">Contact Information</h4>
  <div class="rule" style="left:304px;width:290px"></div>
  <div class="f-contact">
    <div class="row"><svg class="ico" viewBox="0 0 14 14" fill="#fff"><path d="M7 0a5 5 0 0 1 5 5c0 4-5 9-5 9S2 9 2 5a5 5 0 0 1 5-5z"/><circle cx="7" cy="5" r="2" fill="#3a5d99"/></svg><span>ABN 00 123 456 789, Head Office, 4 Harbour Lane, Learning Park, Eastfield 4120<br>PO Box 310 Eastfield DC 4120</span></div>
    <div class="row"><svg class="ico" viewBox="0 0 14 14" fill="#fff"><path d="M3 0l3 3-2 2c1 2 3 4 5 5l2-2 3 3-2 3C6 14 0 8 0 3z"/></svg><span class="phone">FREECALL 1800 555 019</span></div>
    <div class="row"><svg class="ico" viewBox="0 0 14 14" fill="#fff"><rect y="2" width="14" height="10" rx="1"/><path d="M0 3l7 5 7-5" stroke="#3a5d99" fill="none"/></svg><span>info@lendyourlessons.com</span></div>
  </div>
  <h4 style="left:641px">Newsletter Signup</h4>
  <div class="rule" style="left:641px;width:250px"></div>
  <div class="f-news">
    <p>Please enter your email address below to receive our FREE newsletter</p>
    <div class="field">Your Email ID</div>
    <span class="subscribe">Subscribe</span>
  </div>
  <h4 style="left:933px">Follow Us</h4>
  <div class="rule" style="left:933px;width:180px"></div>
  <ul class="f-social">
    <li><span class="sq"></span>Circlebook</li>
    <li><span class="sq"></span>Linkwork</li>
    <li><span class="sq"></span>Chirper</li>
    <li><span class="sq"></span>Email</li>
  </ul>
</footer>

<div class="bottom-bar">
  <span>Copyright@lendyourlessons.com. All Rights Are Reserved.</span>
  <nav><a href="#">Join Us</a><a href="#">Login to lendyourlessons Online</a><a href="#">Support</a></nav>
</div>

</body>
</html>
```